I work in creative/artistic projects across different mediums.
It needs to communicate creativity, style, sexy, uniqueness, individuality and sophistication.
It should not look corporate.
Colours I like are black silver gold deep purple, chocolate, orchid.
It doesn't have to make use of all these colours.
I do not like bright primary colors.
Updates

Project Deadline Extended
Reason: Still in the communication process and to allow the person enough time to finish the design. Though i should know in the next day or two. Thank you.

Target Market(s)

creatives and companies wanting to inject creativity into thier business.

Industry/Entity Type

Work

Contact Information for Business Card

Marcus Tellwick
0418592036
marcus@marcustellwick.com

quietgoldenhour.com.au

Requirements
Should not have
• Anything corporate OR OLD FASHIONED

```html
<!DOCTYPE html>
<html lang="en">
<head>
<meta charset="utf-8">
<title>Marcus Tellwick – Creative consultant</title>
<link rel="stylesheet" href="https://fonts.googleapis.com/css2?family=Montserrat:wght@600;700&family=Questrial&display=swap">
<style>
  :root {
    --stage-light: #ffffff;
    --stage-mist: #e4e6e8;
    --card-black: #000000;
    --ring-chocolate: #775434;
    --ring-mocha: #9b7550;
    --ring-gold: #b5966c;
    --ring-edge: #3a3a3a;
    --ink-white: #ffffff;
    --ink-gold: #b5966c;
    --flourish-grey: #3c3c3c;
  }
  * { margin: 0; padding: 0; box-sizing: border-box; }
  html, body {
    width: 1200px;
    height: 761px;
    overflow: hidden;
  }
  body {
    position: relative;
    background:
      radial-gradient(ellipse 70% 60% at 50% 50%, var(--stage-light) 40%, transparent 100%),
      linear-gradient(135deg, var(--stage-light) 0%, var(--stage-mist) 45%, var(--stage-light) 100%);
  }
  .business-card {
    position: absolute;
    left: 315px;
    top: 217px;
    width: 567px;
    height: 340px;
    overflow: hidden;
    background: var(--card-black);
  }
  .card-art { position: absolute; inset: 0; display: block; }
  .contact-line {
    font-family: "Montserrat", "Century Gothic", sans-serif;
    font-weight: 600;
    font-size: 16.5px;
    fill: var(--ink-white);
    letter-spacing: 0.2px;
  }
  .flourish-area {
    position: absolute;
    left: 290px;
    top: 125px;
    width: 277px;
    height: 215px;
    background: radial-gradient(ellipse 55% 50% at 60% 45%, var(--flourish-grey) 0%, rgba(40,40,40,0.35) 45%, transparent 75%);
    opacity: 0.55;
  }
  .identity {
    position: absolute;
    right: 37px;
    top: 240px;
    text-align: right;
  }
  .identity-name {
    font-family: "Montserrat", "Century Gothic", sans-serif;
    font-weight: 700;
    font-size: 29px;
    line-height: 1;
    color: var(--ink-white);
    letter-spacing: 0.2px;
  }
  .identity-role {
    font-family: "Questrial", "Century Gothic", sans-serif;
    font-size: 19px;
    line-height: 1;
    margin-top: 7px;
    color: var(--ink-gold);
  }
</style>
</head>
<body>
  <section class="business-card">
    <div class="flourish-area" role="img" aria-label="Soft grey swirling flourish ornament"></div>

    <svg class="card-art" width="567" height="340" viewBox="0 0 567 340" xmlns="http://www.w3.org/2000/svg">
      <defs>
        <path id="phone-arc" d="M 0 187 A 222 222 0 0 0 222 -35"/>
        <path id="email-arc" d="M 0 241 A 276 276 0 0 0 276 -35"/>
        <path id="web-arc" d="M 0 308 A 343 343 0 0 0 343 -35"/>
      </defs>

      <g class="rings">
        <circle class="ring-edge" cx="0" cy="-35" r="371" fill="var(--ring-edge)"/>
        <circle class="ring-outer" cx="0" cy="-35" r="368" fill="var(--ring-gold)"/>
        <circle class="ring-edge" cx="0" cy="-35" r="297" fill="var(--ring-edge)"/>
        <circle class="ring-middle" cx="0" cy="-35" r="294" fill="var(--ring-mocha)"/>
        <circle class="ring-edge" cx="0" cy="-35" r="237" fill="var(--ring-edge)"/>
        <circle class="ring-inner" cx="0" cy="-35" r="234" fill="var(--ring-chocolate)"/>
      </g>

      <g class="contact-icons" fill="var(--ink-white)">
        <path class="icon-phone" d="M50 141 c3 -2 5 -1 6 1 l4 7 c1 2 0 4 -2 5 l-2 1 c1 4 5 9 9 11 l2 -2 c1 -1 3 -1 5 0 l6 4 c2 1 2 3 1 5 l-3 3 c-3 3 -10 1 -17 -6 c-7 -7 -12 -16 -10 -22 z"/>
        <g class="icon-mail">
          <rect x="46" y="208" width="33" height="23" fill="var(--ink-white)"/>
          <path d="M46 208 L62.5 222 L79 208" fill="none" stroke="var(--ring-mocha)" stroke-width="2"/>
          <path d="M46 231 L58 219 M79 231 L67 219" fill="none" stroke="var(--ring-mocha)" stroke-width="1.5"/>
        </g>
        <g class="icon-web">
          <circle cx="64" cy="289" r="17" fill="var(--ink-white)"/>
          <ellipse cx="64" cy="289" rx="7" ry="17" fill="none" stroke="var(--ring-gold)" stroke-width="1.6"/>
          <path d="M48 283 H80 M48 295 H80" stroke="var(--ring-gold)" stroke-width="1.6"/>
          <rect x="47" y="285" width="34" height="8" fill="var(--ink-white)"/>
          <text x="64" y="292" text-anchor="middle" font-family="Montserrat, sans-serif" font-weight="700" font-size="8" fill="var(--ring-gold)">www</text>
        </g>
      </g>

      <text class="contact-line contact-phone"><textPath href="#phone-arc" startOffset="112">041 859 2036</textPath></text>
      <text class="contact-line contact-email"><textPath href="#email-arc" startOffset="98">marcus@marcustellwick.com</textPath></text>
      <text class="contact-line contact-web"><textPath href="#web-arc" startOffset="115">www.quietgoldenhour.com.au</textPath></text>
    </svg>

    <div class="identity">
      <h1 class="identity-name">Marcus Tellwick</h1>
      <p class="identity-role">Creative consultant</p>
    </div>
  </section>
</body>
</html>
```